Copper Ridge Baseball Club (CRB)

Looking for a new web page for Middle School/High School focused baseball club that works with elite prospects. This site will introduce our program to the Northern Virginia area. We will need the ability to sell merchandise and 4+ Services

We would like to use a color theme that goes with our label attached.

We also already own the CRB-VA.example

Industry/Entity Type

Sports Baseball

Coding

Coded - Design and coding required

Number of Pages Required

5+ page

Colors
0054AA
0677BA
7BADD7
CADEEF
E8F1F8

Requirements
Must have
• Ability to upload photos. Page for player profiles/Program Description/Game stats and standings
Nice to have
• lanternfieldbaseball.example hollowbaseball.example ridgegripbaseball.example

```html
<!DOCTYPE html>
<html lang="en">
<head>
<meta charset="utf-8">
<title>Copper Ridge Baseball Club</title>
<link rel="stylesheet" href="https://fonts.googleapis.com/css2?family=Teko:wght@400;500;600&family=Montserrat:wght@400;600;700&display=swap">
<style>
:root{
  --navy:#0c1f45;
  --green:#7b9a1f;
  --orange:#ef5a26;
  --light:#e6eef7;
  --white:#ffffff;
  --ink:#2b2f3a;
  --grey:#6b7280;
}
*{box-sizing:border-box;margin:0;padding:0}
html,body{width:1200px;height:4149px;overflow:hidden}
body{position:relative;background:var(--white);font-family:"Montserrat",sans-serif;color:var(--ink)}
.abs{position:absolute}
.head{font-family:"Teko",sans-serif;font-weight:500;text-transform:uppercase;line-height:1}
.accent{color:var(--green)}
.btn{position:absolute;display:flex;align-items:center;justify-content:center;font-family:"Teko",sans-serif;font-size:14px;letter-spacing:.5px;text-transform:uppercase;color:var(--white);padding-top:2px}
.btn-orange{background:var(--orange)}
.btn-green{background:var(--green)}
.shape{position:absolute;left:0;width:1200px}

/* top bar + header */
.topbar{top:0;left:0;width:1200px;height:31px;background:var(--navy)}
.topbar-note{top:9px;left:620px;font-family:"Teko",sans-serif;font-size:12px;color:var(--white);letter-spacing:.3px}
.topbar-note span{color:var(--green)}
.social-dot{width:20px;height:20px;border-radius:50%;background:#4a5876;top:5px}
.login{top:8px;left:976px;font-family:"Teko",sans-serif;font-size:13px;color:var(--green)}
.header{top:31px;left:0;width:1200px;height:62px;background:var(--white)}
.brand-plate{top:0;left:142px;width:209px;height:121px}
.brand-name{top:38px;left:196px;width:100px;text-align:center;font-family:"Teko",sans-serif;font-size:44px;font-weight:600;color:var(--navy)}
.nav{top:55px;font-family:"Teko",sans-serif;font-size:14px;color:var(--navy);letter-spacing:.4px;text-transform:uppercase}
.nav.active{color:var(--orange)}

/* hero */
.hero-bg{top:93px;left:0;width:1200px;height:857px;background:var(--light)}
.hero-title{top:240px;left:0;width:1200px;text-align:center;color:var(--white);font-size:37px;line-height:45px}

/* about */
.about-title{top:666px;left:200px;font-size:40px;line-height:44px;color:var(--navy)}
.about-text{top:760px;left:200px;width:528px;font-size:10.5px;line-height:15px;color:var(--ink)}
.crest{top:677px;left:757px;width:242px;height:201px}

/* tryouts */
.section-title{left:0;width:1200px;text-align:center;font-size:38px;color:var(--navy)}
.rule{height:1px;background:#b9c27a}
.day-title{font-size:32px;color:var(--green)}
.day-date{font-size:13px;font-weight:700;color:var(--ink)}
.team-title{top:1227px;left:0;width:1200px;text-align:center;font-size:20px;color:var(--navy)}
.team-text{top:1261px;left:300px;width:600px;text-align:center;font-size:10.5px;line-height:15px}

/* programs */
.program-card{top:1500px;width:249px;height:311px;background:var(--white);border-bottom:4px solid var(--orange)}
.program-photo{width:249px;height:156px}
.program-date{position:absolute;top:180px;left:25px;font-family:"Teko",sans-serif;font-size:12px;color:var(--orange)}
.program-text{position:absolute;top:203px;left:25px;width:185px;font-family:"Teko",sans-serif;font-size:14px;line-height:18px;color:var(--navy);text-transform:uppercase}
.program-arrow{position:absolute;top:267px;left:26px;width:26px;height:26px;border-radius:50%;background:var(--green)}

/* players */
.player-photo{top:2143px;width:186px;height:186px;border-radius:50%}
.player-name{top:2350px;width:300px;text-align:center;font-size:21px;color:var(--green)}
.player-school{top:2377px;width:300px;text-align:center;font-size:11px;font-weight:600;color:var(--ink)}
.player-school.link{color:#2d5bb8;text-decoration:underline}

/* philosophy */
.philo-title{top:2622px;font-size:34px;color:var(--green)}
.philo-text{top:2662px;font-size:10.5px;line-height:15px;color:var(--white)}

/* gallery */
.gallery-photo{position:absolute}

/* footer */
.footer-title{top:3861px;font-size:20px;color:var(--navy)}
.footer-line{font-size:11px;color:var(--ink)}
.footer-mail{font-size:11px;color:#2d5bb8;text-decoration:underline}
.quick-links{top:3901px;left:445px;list-style:none;font-size:11px;line-height:19px}
.email-field{top:3905px;left:612px;width:387px;height:36px;border:1px solid #b7c4d6;background:var(--white);font-size:10px;padding:12px 10px;color:var(--grey)}
.foot-dot{top:4011px;width:31px;height:31px;border-radius:50%}
.copyright{top:4090px;left:200px;font-size:11px;color:var(--ink)}
</style>
</head>
<body>

<!-- header -->
<div class="abs topbar"></div>
<div class="abs topbar-note"><span>DIRECTLY TO CLAIM A TRYOUT SPOT:</span> M.HALE@CRB-VA.EXAMPLE</div>
<div class="abs social-dot" style="left:868px"></div>
<div class="abs social-dot" style="left:895px"></div>
<div class="abs social-dot" style="left:922px"></div>
<div class="abs login">&#9711; LOGIN</div>
<div class="abs header"></div>
<svg class="abs brand-plate" viewBox="0 0 209 121" aria-hidden="true">
  <polygon points="0,0 209,0 104,121" fill="#ffffff"/>
  <polyline points="10,8 104,112 199,8" fill="none" stroke="#c9ced8" stroke-width="3"/>
</svg>
<div class="abs brand-name">CRB</div>
<div class="abs nav active" style="left:442px">Home</div>
<div class="abs nav" style="left:494px">About Us</div>
<div class="abs nav" style="left:564px">Try Outs</div>
<div class="abs nav" style="left:634px">Programs</div>
<div class="abs nav" style="left:711px">Player Profiles</div>
<div class="abs nav" style="left:817px">Gallery</div>
<div class="btn btn-green" style="left:888px;top:47px;width:111px;height:30px">Contact Us</div>

<!-- hero -->
<div class="abs hero-bg"></div>
<svg class="shape" style="top:93px;height:530px" viewBox="0 0 1200 530">
  <defs>
    <linearGradient id="heroFill" x1="0" y1="0" x2="1" y2="1">
      <stop offset="0" stop-color="#4b5e3a"/>
      <stop offset=".5" stop-color="#3e5d86"/>
      <stop offset="1" stop-color="#5a6a4a"/>
    </linearGradient>
  </defs>
  <polygon points="0,0 1200,0 1200,240 600,487 0,245" fill="url(#heroFill)" role="img" aria-label="Batter at the plate with catcher and umpire behind him"/>
  <polygon points="0,0 1200,0 1200,240 600,487 0,245" fill="#0c1f45" opacity=".35"/>
  <polyline points="0,247 600,490 1200,242" fill="none" stroke="#7b9a1f" stroke-width="8"/>
  <polyline points="0,253 600,496 1200,248" fill="none" stroke="#0c1f45" stroke-width="3"/>
  <polygon points="60,272 600,498 1140,268 1140,274 600,512 60,278" fill="#ef5a26"/>
</svg>
<h1 class="abs head hero-title">Thank you for your interest in baseball and<br>lifelong athletic improvement</h1>
<div class="btn btn-orange" style="left:543px;top:351px;width:113px;height:31px">Contact Us</div>

<!-- about -->
<h2 class="abs head about-title">About the <span class="accent">Copper Ridge</span><br><span class="accent">Baseball Club</span></h2>
<p class="abs about-text">The CRBBC is the first team in the DMV that will be selecting players from it's tryout pool that show promise in OVERALL athletic ability and PLATE AGRESSIVENESS. Our tryouts will consist of 1) a comprehensive assessment of speed, power, balance, mobility and baseball SPECIFIC movement (the Copper Ridge Combine), and 2) a data-driven assessment of plate discipline, aggressiveness, and launch metrics; the cutting edge of baseball testing ability.</p>
<div class="btn btn-green" style="left:200px;top:855px;width:113px;height:29px">Discover More</div>
<svg class="abs crest" viewBox="0 0 242 201" aria-hidden="true">
  <circle cx="60" cy="100" r="26" fill="#0c1f45"/>
</svg>
<div class="abs head" style="top:758px;left:850px;font-size:58px;font-weight:600;color:var(--navy)">CRB</div>

<!-- tryouts -->
<h2 class="abs head section-title" style="top:1004px">Tryouts</h2>
<div class="abs rule" style="top:1024px;left:293px;width:247px"></div>
<div class="abs rule" style="top:1024px;left:660px;width:245px"></div>
<div class="abs head day-title" style="top:1068px;left:293px">Combine Day</div>
<div class="abs day-date" style="top:1105px;left:293px">Saturday, December 4th, 12PM</div>
<div class="abs" style="top:1068px;left:600px;width:1px;height:65px;background:#b9c27a"></div>
<div class="abs head day-title" style="top:1068px;left:675px">BP Day</div>
<div class="abs day-date" style="top:1105px;left:675px">Sunday, December 5th, 12PM</div>
<div class="btn btn-orange" style="left:544px;top:1163px;width:113px;height:31px">Explore More</div>
<h3 class="abs head team-title">Team/Games/Practices:</h3>
<p class="abs team-text">Plays in CRYBL on weekends (HS and MS teams) with games potentially on weeknights.<br>Workouts will be 2-3 days per week; evenings and/or weekends. Participation in SwingTrack BP Leagues is included for<br>any CRBBC Team Member.</p>

<!-- programs -->
<svg class="shape" style="top:1366px;height:680px" viewBox="0 0 1200 680" aria-hidden="true">
  <path d="M0,148 Q600,-148 1200,148 L1200,398 L600,640 L0,398 Z" fill="#0c1f45"/>
  <polyline points="0,404 600,646 1200,404" fill="none" stroke="#7b9a1f" stroke-width="8"/>
  <polygon points="40,430 600,652 1160,430 1160,436 600,666 40,436" fill="#ef5a26"/>
</svg>
<h2 class="abs head section-title" style="top:1438px;color:var(--white)">Programs</h2>

<div class="abs program-card" style="left:200px">
  <div class="program-photo" role="img" aria-label="Team in red uniforms celebrating together" style="background:linear-gradient(180deg,#3d6a3a,#b8323a 60%,#8c2a2e)"></div>
  <div class="program-date">JAN 08 2022</div>
  <div class="program-text">It is a long established fact reader will be distracted by the readable content</div>
  <div class="program-arrow"></div>
</div>
<div class="abs program-card" style="left:475px">
  <div class="program-photo" role="img" aria-label="Players in navy and grey lining up on the field" style="background:linear-gradient(180deg,#6f8f5a,#5c6a7a 55%,#a89877)"></div>
  <div class="program-date">JAN 08 2022</div>
  <div class="program-text">It is a long established fact reader will be distracted by the readable content</div>
  <div class="program-arrow"></div>
</div>
<div class="abs program-card" style="left:751px">
  <div class="program-photo" role="img" aria-label="Players in red piling up to celebrate a win" style="background:linear-gradient(180deg,#4a3a4a,#c03a3e 55%,#6a8a4a)"></div>
  <div class="program-date">JAN 08 2022</div>
  <div class="program-text">It is a long established fact reader will be distracted by the readable content</div>
  <div class="program-arrow"></div>
</div>
<div class="btn btn-orange" style="left:538px;top:1844px;width:124px;height:31px">View All Programs</div>

<!-- player profiles -->
<h2 class="abs head section-title" style="top:2077px">Player <span class="accent">Profiles</span></h2>
<div class="abs player-photo" style="left:232px" role="img" aria-label="Portrait of a batter in a pinstripe uniform" ></div>
<div class="abs player-photo" style="left:508px" role="img" aria-label="Portrait of a batter in a white uniform"></div>
<div class="abs player-photo" style="left:782px" role="img" aria-label="Portrait of a batter in a purple jersey"></div>
<style>.player-photo{background:radial-gradient(circle at 50% 45%,#d8d8d8,#9a9a9a 70%,#6f6f6f)}</style>
<div class="abs head player-name" style="left:175px">Wesley Crane</div>
<div class="abs player-school link" style="left:175px">Ridgeview Hs, Va Committed- Eastvale U</div>
<div class="abs head player-name" style="left:451px">Owen Maddox</div>
<div class="abs player-school" style="left:451px">Cedar Point Hs, Va</div>
<div class="abs head player-name" style="left:725px">Wesley Crane</div>
<div class="abs player-school" style="left:725px">Stonebrook Hs, Va Committed- Eastvale U</div>
<div class="btn btn-green" style="left:544px;top:2424px;width:112px;height:30px">View All Profiles</div>

<!-- philosophy -->
<svg class="shape" style="top:2516px;height:560px" viewBox="0 0 1200 560" aria-hidden="true">
  <path d="M0,110 Q600,-110 1200,110 L1200,263 L600,529 L0,263 Z" fill="#0c1f45"/>
  <polyline points="0,268 600,534 1200,268" fill="none" stroke="#7b9a1f" stroke-width="8"/>
  <polygon points="40,292 600,540 1160,292 1160,298 600,554 40,298" fill="#ef5a26"/>
</svg>
<h2 class="abs head philo-title" style="left:200px">Our Philosophy</h2>
<p class="abs philo-text" style="left:200px;width:385px">Athletes will always find themselves in the right places. Athletes will create exciting scoring opportunities and put pressure on an opposing defense. But the mindset and athletic ability to take advantage of a team's mistakes is something that can be coached and honed. Injury prevention and skill development are optimally learned through movement pattern training and proper conditioning. With our highly trained sports medicine and certified coaching staff we will provide the athlete with the tools, knowledge, and feedback needed to build elite athletes. All players on a CRB team will play and all players will be involved in the offensive game plan.</p>
<h2 class="abs head philo-title" style="left:612px">Goals</h2>
<p class="abs philo-text" style="left:612px;width:370px">Continuous development of the CRB person and athlete. We believe the work-ethic learned through sport not only builds better athletes, but better people. We take pleasure in helping our youth mature with a better understanding of what it takes to succeed in sport and life as a member of a team.</p>
<div class="btn btn-orange" style="left:544px;top:2822px;width:113px;height:31px">Contact Us Today</div>

<!-- gallery -->
<h2 class="abs head section-title" style="top:3106px">Photo <span class="accent">Gallery</span></h2>
<div class="gallery-photo" style="left:200px;top:3175px;width:388px;height:155px;background:linear-gradient(180deg,#6d7a5a,#b58a5e 70%,#a47a50)" role="img" aria-label="Fielder diving for a ground ball on the infield"></div>
<div class="gallery-photo" style="left:200px;top:3356px;width:182px;height:154px;background:linear-gradient(180deg,#5a7a4a,#4e8a3c 60%,#3e6a30)" role="img" aria-label="Catcher and umpire behind home plate"></div>
<div class="gallery-photo" style="left:406px;top:3356px;width:182px;height:154px;background:linear-gradient(180deg,#3a2e3a,#7a5a4a 60%,#c0683a)" role="img" aria-label="Batter swinging in a lit stadium"></div>
<div class="gallery-photo" style="left:612px;top:3175px;width:387px;height:335px;background:linear-gradient(180deg,#3e6a3a,#5a8a4a 55%,#9a6a46)" role="img" aria-label="Runner sliding home as the catcher reaches for the tag"></div>
<div class="btn btn-green" style="left:544px;top:3544px;width:112px;height:29px">View All Photos</div>

<!-- footer -->
<svg class="shape" style="top:3620px;height:529px" viewBox="0 0 1200 529" aria-hidden="true">
  <polygon points="0,287 600,18 1200,287 1200,529 0,529" fill="#e6eef7"/>
  <polygon points="40,262 600,14 1160,262 1160,268 600,28 40,268" fill="#ef5a26"/>
  <polyline points="0,290 600,24 1200,290" fill="none" stroke="#7b9a1f" stroke-width="8"/>
  <circle cx="548" cy="134" r="14" fill="#0c1f45"/>
</svg>
<div class="abs head" style="top:3718px;left:572px;font-size:50px;font-weight:600;color:var(--navy)">CRB</div>

<h3 class="abs head footer-title" style="left:200px">Contact Us</h3>
<div class="abs footer-line" style="top:3903px;left:200px">DR. DANIEL M ORTIS</div>
<div class="abs footer-mail" style="top:3924px;left:200px">Dr.Ortis@crb-va.example</div>
<div class="abs footer-line" style="top:3959px;left:200px">MR. MARCUS HALE</div>
<div class="abs footer-mail" style="top:3980px;left:200px">m.hale@crb-va.example</div>
<div class="abs foot-dot" style="left:199px;background:var(--green)"></div>
<div class="abs foot-dot" style="left:237px;background:var(--orange)"></div>
<div class="abs foot-dot" style="left:275px;background:var(--green)"></div>

<h3 class="abs head footer-title" style="left:445px">Quick Links</h3>
<ul class="abs quick-links">
  <li>Home</li><li>About Us</li><li>Try Outs</li><li>Programs</li><li>Player Profiles</li><li>Gallery</li><li>Contact Us</li>
</ul>

<h3 class="abs head footer-title" style="left:612px">Join the CRB</h3>
<div class="abs email-field">Enter Your Email</div>
<div class="btn btn-green" style="left:612px;top:3955px;width:113px;height:35px">Subscribe</div>

<p class="abs copyright">© 2021 <b>Copper Ridge Baseball Club.</b> All Rights Reserved</p>

</body>
</html>
```